Kellwood Build, Carpentry Services

Business card for carpentry business in the Sunshine Coast.

Business card layout required using logo provided - provided both PDF copy and AI. Please let me know if you would like a the files for the logo symbol and text by itself.

Business Colours are grey, blue and white. The font colours codes for this design are Blue Hex # 00B4E6 and Hex # 39393B for the gray colour.

FYI font for logo is Gotham Bold.

Preference for a clean and striking layout that is simple and elegant.

Target Market(s)

Young Families, retirees, young couples requiring assistance with small to medium works/renovations on the Sunshine Coast.

Industry/Entity Type

Construction

Contact Information for Business Card

Dean Kellwood
Carpenter
0489305627
dean@kellwoodbuild.com.au
Brindale Heads, Coral Coast
RHPA Licensed Carpenter (In smaller font)

Font styles to use
Sans Serif

Colors

Designer to choose colors to be used in the design.

Requirements
Must have
• Logo provided must appear on the card, preferably on one side of the card by itself with the text on the alternate side
Nice to have
• Text on the other side of card, maybe grey background and white font here but happy for the designer to provide ideas here.
Should not have
• Use of other colours, other than the ones provided - white, grey and blue. Black optional.

```html
<!DOCTYPE html>
<html lang="en">
<head>
<meta charset="UTF-8">
<title>Kellwood Build – Business Card</title>
<link rel="stylesheet" href="https://fonts.googleapis.com/css2?family=Montserrat:wght@400;500;700&display=swap">
<style>
  :root {
    --blue: #00B4E6;
    --grey: #39393B;
    --white: #FFFFFF;
    --backdrop: #1c1c1d;
    --muted: #d9d9da;
  }
  * { margin: 0; padding: 0; box-sizing: border-box; }
  html, body { width: 1200px; height: 900px; overflow: hidden; }
  body {
    background: var(--backdrop);
    font-family: "Montserrat", sans-serif;
    display: flex;
    flex-direction: column;
    align-items: center;
    justify-content: center;
    gap: 36px;
  }
  .card {
    position: relative;
    width: 740px;
    height: 404px;
    background: var(--grey);
    overflow: hidden;
  }
  /* Front: brand name alone */
  .card-front {
    display: flex;
    align-items: center;
    justify-content: center;
  }
  .brand-name {
    font-weight: 700;
    color: var(--blue);
    text-transform: uppercase;
    letter-spacing: 0.04em;
    display: flex;
    align-items: center;
  }
  .brand-mark {
    display: inline-block;
    background: var(--blue);
    border-radius: 50%;
  }
  .card-front .brand-name { font-size: 44px; gap: 18px; }
  .card-front .brand-mark { width: 22px; height: 22px; }

  /* Back: details */
  .card-back .brand-name {
    position: absolute;
    top: 44px;
    left: 44px;
    font-size: 28px;
    gap: 12px;
  }
  .card-back .brand-mark { width: 14px; height: 14px; }
  .divider {
    position: absolute;
    top: 244px;
    left: 56px;
    right: 56px;
    height: 1px;
    background: var(--muted);
  }
  .person {
    position: absolute;
    top: 258px;
    left: 44px;
    color: var(--white);
  }
  .person-name {
    font-weight: 700;
    font-size: 29px;
    color: var(--blue);
    text-transform: uppercase;
    letter-spacing: 0.02em;
    line-height: 1.1;
  }
  .person-title { font-size: 20px; font-weight: 500; margin-top: 2px; }
  .person-licence { font-size: 15px; font-weight: 400; margin-top: 4px; color: var(--muted); }

  .contact {
    position: absolute;
    right: 44px;
    top: 276px;
    list-style: none;
    color: var(--white);
    font-size: 18px;
    text-align: right;
  }
  .contact li {
    display: flex;
    align-items: center;
    justify-content: flex-end;
    gap: 10px;
    line-height: 1.5;
  }
  .contact svg { width: 18px; height: 18px; flex-shrink: 0; }

  .accent-band {
    position: absolute;
    left: 0;
    bottom: 0;
    width: 56%;
    height: 22px;
    background: var(--blue);
  }
  .base-band {
    position: absolute;
    left: 56%;
    right: 0;
    bottom: 0;
    height: 8px;
    background: var(--white);
  }
</style>
</head>
<body>
  <section class="card card-front">
    <div class="brand-name"><span class="brand-mark"></span>Kellwood Build</div>
  </section>

  <section class="card card-back">
    <div class="brand-name"><span class="brand-mark"></span>Kellwood Build</div>

    <div class="divider"></div>

    <div class="person">
      <p class="person-name">Dean Kellwood</p>
      <p class="person-title">Carpenter</p>
      <p class="person-licence">RHPA Licensed Carpenter</p>
    </div>

    <ul class="contact">
      <li>0489 305 627
        <svg viewBox="0 0 24 24" fill="none" stroke="var(--blue)" stroke-width="2"><circle cx="12" cy="12" r="10"/><path d="M8.5 7.5c0 4.5 3.5 8 8 8l1-2-2.5-1.2-1 1c-1.5-.6-2.7-1.8-3.3-3.3l1-1L10.5 6.5z"/></svg>
      </li>
      <li>dean@kellwoodbuild.com.au
        <svg viewBox="0 0 24 24" fill="none" stroke="var(--blue)" stroke-width="2"><rect x="2" y="5" width="20" height="14"/><path d="M2 5l10 8 10-8"/></svg>
      </li>
      <li>Brindale Heads, Coral Coast
        <svg viewBox="0 0 24 24" fill="var(--blue)"><path d="M12 2L1 12h3v10h6v-6h4v6h6V12h3z"/></svg>
      </li>
    </ul>

    <div class="accent-band"></div>
    <div class="base-band"></div>
  </section>
</body>
</html>
```